Harbor Lantern Podcast needs fun, creative cover art

Launching a new podcast called 'Opening Windows Toward Brighter Days' - aimed at an audience 30-50 who are interested in the practicalities of managing their money but also the more mental and emotional aspects.
Looking for something not too serious, warm and friendly.

Must be easy to read on phone screens
3000 x 3000 in size
Avoid currency symbols $, £ etc, as may have an international audience

Target Market(s)

Podcast listeners age 30-50 starting in the UK but then worldwide. Probably 60:40 female bias

Industry/Entity Type

Life Coaching

Font styles to use
Serif
Sans Serif

Colors
cadf82
fee18a
acd037
85cae6
eea4c8
f59195
85acd3

Requirements
Must have
• Simple, clear design. Easy to read on variety of devices. 3000 x 3000
Appeal to those with a spiritual or emotional interests
Nice to have
• Stand out among other money related podcasts
Maybe play around with clouds, lightbulbs and clearing skies
Should not have
• Currency symbols such as $ or £
Be too corporate or bank like
Stock images

```html
<!DOCTYPE html>
<html lang="en">
<head>
<meta charset="utf-8">
<title>Opening Windows Toward Brighter Days — Podcast Cover</title>
<link rel="stylesheet" href="https://fonts.googleapis.com/css2?family=Barlow+Condensed:wght@500;600&display=swap">
<style>
  :root {
    --bg: #000000;
    --green-bright: #8ccf2c;
    --green-deep: #78ae26;
    --white: #ffffff;
  }
  html, body {
    margin: 0;
    padding: 0;
    width: 1200px;
    height: 1200px;
    overflow: hidden;
    background: var(--bg);
  }
  .cover {
    display: block;
    width: 1200px;
    height: 1200px;
  }
  .title-text {
    font-family: "Barlow Condensed", sans-serif;
    font-weight: 600;
  }
  .title-top { fill: var(--green-bright); }
  .title-middle { fill: var(--white); }
  .title-bottom { fill: var(--green-deep); }
  .divider { fill: var(--white); }
  .listen-line {
    font-family: "Barlow Condensed", sans-serif;
    font-weight: 600;
    fill: var(--white);
  }
</style>
</head>
<body>
<svg class="cover" viewBox="0 0 1200 1200" xmlns="http://www.w3.org/2000/svg" role="img" aria-label="Opening Windows Toward Brighter Days podcast cover">
  <rect width="1200" height="1200" fill="var(--bg)"/>

  <g class="title">
    <text class="title-text title-top" x="156" y="408" font-size="279" textLength="849" lengthAdjust="spacingAndGlyphs">OPENING</text>
    <text class="title-text title-middle" x="157" y="531" font-size="150" textLength="848" lengthAdjust="spacingAndGlyphs">WINDOWS TOWARD BRIGHTER</text>
    <text class="title-text title-bottom" x="175" y="822" font-size="398" textLength="809" lengthAdjust="spacingAndGlyphs">DAYS</text>
  </g>

  <rect class="divider" x="0" y="921" width="1200" height="7"/>

  <text class="listen-line" x="189" y="1040" font-size="86" textLength="822" lengthAdjust="spacingAndGlyphs">PODCAST LISTEN ON TIDECAST</text>
</svg>
</body>
</html>
```